https://copperwillowbrambleyard.org/

We would like the website to represent 19th century African American civil war soldier's letters. We would like the site colors to be nice and clean . Along with the layout, including a great landing page , blogs and introduction.

```html
<!DOCTYPE html>
<html lang="en">
<head>
<meta charset="utf-8">
<title>CWB. — Story of The Week</title>
<link href="https://fonts.googleapis.com/css2?family=Roboto:wght@300;400;500;700&display=swap" rel="stylesheet">
<style>
:root{
  --paper:#F0EBE1;
  --ink:#2F2D2B;
  --ink-soft:#5E5A55;
  --tan:#C9A688;
  --rule:#CDB395;
  --rule-grey:#A8A49D;
  --slate:#5B6E7A;
  --heart:#C0392B;
}
*{box-sizing:border-box;margin:0;padding:0}
html,body{width:1200px;height:1172px;overflow:hidden;background:var(--paper)}
body{position:relative;font-family:'Roboto',sans-serif;color:var(--ink)}
.abs{position:absolute}
.brand{left:0;width:1200px;text-align:center;font-weight:700;font-size:26px;letter-spacing:1px;color:var(--ink)}
.brand--top{top:38px}
.brand--foot{top:1037px}
.nav{top:97px;left:469px;display:flex;gap:33px;font-size:13.5px;color:var(--ink-soft)}
.nav a{color:inherit;text-decoration:none;position:relative}
.nav a.is-active{color:var(--ink);font-weight:500}
.nav a.is-active::after{content:"";position:absolute;left:0;top:22px;width:31px;height:1px;background:var(--ink)}
.nav a.is-active::before{content:"";position:absolute;left:33px;top:21px;width:2.5px;height:2.5px;border-radius:50%;background:var(--ink)}
.search{left:1080px;top:96px}
.rule{left:100px;width:1000px;height:1px;background:var(--rule)}
.rule--grey{background:var(--rule-grey)}
.sort-label{left:100px;top:199px;font-size:12.5px;color:var(--ink-soft)}
.sort-value{left:100px;top:219px;font-size:20px;font-weight:500}
.section-title{left:99px;top:281px;font-size:48px;font-weight:300;letter-spacing:.2px}
.frame{border:1px solid var(--tan)}
.block{background:var(--slate)}
.photo{position:absolute}
.photo--birds{background:linear-gradient(180deg,#cfcfcf 0%,#9d9d9d 45%,#555 80%,#1e1e1e 100%)}
.photo--ride{background:linear-gradient(180deg,#e8e8e8 0%,#cfcfcf 30%,#6d6d6d 55%,#7f7f7f 75%,#5c5c5c 100%)}
.meta{font-size:11.5px;color:var(--ink-soft)}
.quote{font-size:26.5px;line-height:32px;color:var(--ink);white-space:nowrap}
.arrow{left:670px;top:565px}
.social{top:1096px;left:0;width:1200px;display:flex;justify-content:center;gap:28px;font-size:14px;color:var(--ink-soft)}
.social span{display:flex;align-items:center;gap:7px}
.social i{display:inline-block;width:20px;height:20px;border:1.4px solid var(--ink-soft);border-radius:50%}
.copyright{top:1131px;left:0;width:1200px;text-align:center;font-size:11.5px;color:var(--ink-soft)}
.copyright b{color:var(--heart);font-weight:400}
</style>
</head>
<body>
<header>
  <div class="abs brand brand--top">CWB.</div>
  <nav class="abs nav">
    <a class="is-active" href="#">Home</a>
    <a href="#">Stories</a>
    <a href="#">About</a>
    <a href="#">Contact</a>
  </nav>
  <svg class="abs search" width="20" height="20" viewBox="0 0 20 20" fill="none" stroke="#2F2D2B" stroke-width="1.3"><circle cx="8" cy="8" r="6.5"/><line x1="12.8" y1="12.8" x2="18.5" y2="18.5"/></svg>
  <div class="abs rule" style="top:152px"></div>
  <div class="abs rule" style="top:165px"></div>
</header>

<main>
  <div class="abs sort-label">Sort By &nbsp;<svg width="9" height="12" viewBox="0 0 9 12" fill="none" stroke="#5E5A55" stroke-width="1.2"><line x1="4.5" y1="0" x2="4.5" y2="11"/><polyline points="1,7.5 4.5,11 8,7.5"/></svg></div>
  <div class="abs sort-value">Popularity</div>
  <h1 class="abs section-title">Story of The Week.</h1>

  <article class="story">
    <div class="abs block" style="left:335px;top:400px;width:268px;height:294px"></div>
    <div class="abs frame" style="left:127px;top:413px;width:463px;height:308px"></div>
    <div class="abs frame" style="left:100px;top:427px;width:477px;height:470px"></div>
    <div class="photo photo--birds" role="img" aria-label="Misty black and white landscape with birds in flight over trees" style="left:113px;top:440px;width:450px;height:313px"></div>
    <div class="abs meta" style="left:113px;top:767px">Marla22</div>
    <div class="abs meta" style="left:413px;width:150px;text-align:right;top:767px">20 Feb ' 2020</div>
    <p class="abs quote" style="left:113px;top:812px">"I have not heard from Brother Amos<br>since I wrote to you"</p>
  </article>

  <svg class="abs arrow" width="102" height="10" viewBox="0 0 102 10" fill="none" stroke="#4A4744" stroke-width="1"><line x1="0" y1="5" x2="100" y2="5"/><polyline points="95,2 100,5 95,8"/></svg>

  <article class="story">
    <div class="abs block" style="left:1072px;top:400px;width:140px;height:60px"></div>
    <div class="abs frame" style="left:843px;top:413px;width:400px;height:308px"></div>
    <div class="abs frame" style="left:823px;top:427px;width:420px;height:470px"></div>
    <div class="photo photo--ride" role="img" aria-label="Motorcyclist riding along an open road under a grey sky" style="left:837px;top:440px;width:380px;height:313px"></div>
    <div class="abs meta" style="left:837px;top:767px">Marla22</div>
    <p class="abs quote" style="left:837px;top:812px">“I’m well and doing well as a soldier<br>can expect...”</p>
  </article>
</main>

<footer>
  <div class="abs rule rule--grey" style="top:983px"></div>
  <div class="abs rule rule--grey" style="top:996px"></div>
  <div class="abs brand brand--foot">CWB.</div>
  <div class="abs social">
    <span><i></i>Shutterfeed</span>
    <span><i></i>Townsquare</span>
  </div>
  <p class="abs copyright">© 2020 copperwillowbrambleyard.org. Made with <b>♡</b> from Virginia</p>
</footer>
</body>
</html>
```